Batch #27 - MEN'S NATURAL THERAPEUTIC INTIMATE WASH

Men's Natural Therapeutic INTIMATE Wash
BATCH #27

Design a 4 oz. stand up tube with flip top cap...
To be packaged in a carton/box

Formula contains Tea Tree OIL
Aloe Vera Gel
Coconut Oil

PRODUCT IS A WASH/SOAP

Helps with
- Jock Itch (tinea cruris)
- Skin Rashes
- Candida
- Itchy Skin

COLORS ON TUBE: Gray, Black, Lime Electric Green and Blue

PRODUCT FOR MEN!

Target Market(s)

MEN

Industry/Entity Type

Retail

Font styles to use
Sans Serif

Colors
9bcb3b
abd036
33a6d7
000000
c9c9c9

Requirements
Must have
• Colors... black, gray, electric green and blue
Nice to have
• Needs to look masculine appeal to the male consumer

```html
<!DOCTYPE html>
<html lang="en">
<head>
<meta charset="utf-8">
<title>Batch #27 – Men's Natural Therapeutic Intimate Wash</title>
<link rel="stylesheet" href="https://fonts.googleapis.com/css2?family=Montserrat:wght@600;700;800&family=Space+Mono&display=swap">
<style>
  :root {
    --ink: #1a1a1a;
    --dark-text: #111111;
    --white: #ffffff;
    --lime: #9bcb3b;
    --lime-bright: #abd036;
    --blue: #33a6d7;
    --gray: #c9c9c9;
  }
  * { margin: 0; padding: 0; box-sizing: border-box; }
  html, body { width: 872px; height: 1200px; overflow: hidden; background: var(--ink); }
  .package {
    position: relative;
    width: 872px;
    height: 1200px;
    background: var(--ink);
    font-family: "Montserrat", Arial, sans-serif;
    color: var(--white);
    overflow: hidden;
  }
  .package__shapes { position: absolute; inset: 0; }

  .brand-name {
    position: absolute;
    left: 34px;
    top: 52px;
    font-size: 140px;
    font-weight: 700;
    line-height: 1;
    letter-spacing: 10px;
  }
  .brand-number {
    position: absolute;
    right: 20px;
    top: 232px;
    font-size: 176px;
    font-weight: 700;
    line-height: 1;
    letter-spacing: 2px;
  }
  .band-title {
    position: absolute;
    left: 468px;
    top: 612px;
    transform: translate(-50%, -50%) rotate(45.8deg);
    white-space: nowrap;
    font-size: 27px;
    font-weight: 600;
    color: var(--dark-text);
  }
  .badge-number {
    position: absolute;
    left: 100px;
    top: 630px;
    font-size: 104px;
    font-weight: 600;
    line-height: 1;
    color: var(--dark-text);
  }
  .benefits {
    position: absolute;
    left: 104px;
    top: 752px;
  }
  .benefits__title {
    font-size: 31px;
    font-weight: 600;
    letter-spacing: 1px;
    line-height: 1;
    margin-bottom: 14px;
  }
  .benefits__list {
    list-style: none;
    font-family: "Space Mono", "Courier New", monospace;
    font-size: 24px;
    line-height: 45px;
  }
  .ingredients__label {
    position: absolute;
    left: 71px;
    top: 1029px;
    width: 400px;
    height: 53px;
    background: var(--lime);
    color: var(--dark-text);
    font-size: 27px;
    font-weight: 700;
    letter-spacing: 2px;
    line-height: 53px;
    padding-left: 26px;
  }
  .ingredients__list {
    list-style: none;
    position: absolute;
    top: 1094px;
    left: 0;
    width: 872px;
    font-size: 24px;
    font-weight: 600;
    line-height: 32px;
  }
  .ingredients__item { position: absolute; white-space: nowrap; }
  .ingredients__item::before { content: "•"; margin-right: 14px; }
  .ingredients__item--coconut { left: 97px; }
  .ingredients__item--tea-tree { left: 360px; }
  .ingredients__item--aloe { left: 610px; }
</style>
</head>
<body>
<main class="package">
  <svg class="package__shapes" width="872" height="1200" viewBox="0 0 872 1200" aria-hidden="true">
    <rect class="accent-rule accent-rule--vertical" x="67" y="196" width="8" height="1004" fill="var(--lime)"/>
    <rect class="accent-rule accent-rule--horizontal" x="0" y="1004" width="872" height="8" fill="var(--lime)"/>
    <polygon class="diagonal-band" points="97,262 149,262 786,914 786,969" fill="var(--blue)"/>
    <polygon class="corner-triangle" points="97,414 97,741 424,741" fill="var(--lime-bright)"/>
    <line class="side-rule" x1="833" y1="524" x2="833" y2="786" stroke="var(--gray)" stroke-width="3"/>
    <g class="dot-cluster" fill="var(--white)">
      <circle cx="752" cy="406" r="5"/>
      <circle cx="786" cy="406" r="5"/>
      <circle cx="820" cy="406" r="5"/>
      <circle cx="786" cy="440" r="5"/>
      <circle cx="820" cy="440" r="5"/>
      <circle cx="820" cy="474" r="5"/>
    </g>
  </svg>

  <h1 class="brand-name">BATCH</h1>
  <p class="brand-number">#27</p>

  <p class="band-title">Men's Natural Therapeutic INTIMATE Wash</p>
  <p class="badge-number">#27</p>

  <section class="benefits">
    <h2 class="benefits__title">HELP WITH</h2>
    <ul class="benefits__list">
      <li>- Jock Itch (tinea cruris)</li>
      <li>- Skin Rashes</li>
      <li>- Candida</li>
      <li>- Itchy Skin</li>
    </ul>
  </section>

  <section class="ingredients">
    <h2 class="ingredients__label">FORMULA CONTAINS</h2>
    <ul class="ingredients__list">
      <li class="ingredients__item ingredients__item--coconut">Coconut Oil</li>
      <li class="ingredients__item ingredients__item--tea-tree">Tea Tree OIL</li>
      <li class="ingredients__item ingredients__item--aloe">Aloe Vera Gel</li>
    </ul>
  </section>
</main>
</body>
</html>
```